need a graphic redesign of kelvorahomecare.com

Need a graphic redesign of kelvorahomecare.com. We need to make it more user friendly as well as SEO friendly. All information is there. We have lot of stock photos (done our own photoshoot).

We want this website to be redesigned from scratch. Please avoid using pre made templates. Recommend people who really understand design to approach this project.

Target population is Non resident Indians who live outside India but their families are still in India and need for health care.

Logos and pictures are on the website but we can provide raw images.

Target Market(s)

Industry/Entity Type

Healthcare

Number of Pages Required

5+ page

Font styles to use
Serif
Sans Serif

Requirements
Must have
• Good design, and use of minimal text. Design need to be responsive (we know it is a later process in coding- but mobile devices need to be kept in mind)
Nice to have
• We need a original design.
Should not have
• prebuilt or copied templates

```html
<!DOCTYPE html>
<html lang="en">
<head>
<meta charset="utf-8">
<title>Kelvora Home Care</title>
<link href="https://fonts.googleapis.com/css2?family=Open+Sans:wght@400;600;700&family=Roboto+Slab:wght@400;700&display=swap" rel="stylesheet">
<style>
:root{
  --green:#3d9a40;
  --green-dark:#2f7f33;
  --orange:#f7941d;
  --text:#555;
  --heading:#3d9a40;
  --light:#f1f1f1;
  --footer:#262626;
  --white:#fff;
  --red:#e53935;
}
*{box-sizing:border-box;margin:0;padding:0}
html,body{width:1200px;height:3368px;overflow:hidden}
body{font-family:"Open Sans",Arial,sans-serif;color:var(--text);background:#fff;font-size:13px;line-height:1.55}
h1,h2,h3{font-family:"Roboto Slab",Georgia,serif;font-weight:700}
h4{font-family:"Open Sans",Arial,sans-serif;font-weight:700}
.wrap{width:1120px;margin:0 auto;position:relative}
.btn{display:inline-block;background:var(--orange);color:#fff;font-size:12px;font-weight:600;padding:8px 22px;text-transform:uppercase}
.more{color:var(--orange);font-size:11px;font-weight:700;text-transform:uppercase}
.section-title{text-align:center;color:var(--heading);font-size:34px;margin-bottom:26px}
.ph{display:block;position:relative;overflow:hidden}

/* header */
.topbar{height:112px;display:flex;align-items:center}
.brand{display:flex;align-items:center;gap:12px}
.brand-dot{width:40px;height:40px;border-radius:50%;background:var(--orange);flex:none}
.brand-name{font-weight:700;font-size:24px;color:var(--green)}
.top-right{margin-left:auto;display:flex;align-items:center;gap:18px}
.call small{display:block;font-size:11px;color:#777}
.call strong{font-size:20px;color:var(--green)}
.nav{height:48px;background:var(--green)}
.nav ul{list-style:none;display:flex;height:48px;align-items:center;gap:46px;color:#fff;font-size:13px;font-weight:600;text-transform:uppercase}
.nav ul li:first-child{background:var(--green-dark);padding:14px 18px}

/* hero */
.hero{height:600px;position:relative;
  background:
   radial-gradient(ellipse 260px 320px at 70% 45%,rgba(255,255,255,.75),transparent 70%),
   radial-gradient(ellipse 220px 260px at 46% 30%,rgba(226,196,170,.8),transparent 70%),
   radial-gradient(ellipse 300px 200px at 88% 80%,rgba(120,150,170,.7),transparent 70%),
   radial-gradient(ellipse 380px 260px at 15% 85%,rgba(140,170,160,.7),transparent 70%),
   linear-gradient(110deg,#b8ccc6,#e9e1d6 50%,#a9b9bf)}
.hero-circle{position:absolute;left:140px;top:120px;width:400px;height:360px;border-radius:50%;background:rgba(61,154,64,.93);color:#fff;text-align:center;padding:74px 46px}
.hero-circle h1{font-size:32px;margin-bottom:14px}
.hero-circle p{font-size:13px;margin-bottom:22px}
.quote-form{position:absolute;right:40px;top:120px;width:300px;background:#fff;border-top:40px solid var(--green-dark);padding:16px;box-shadow:0 4px 14px rgba(0,0,0,.15)}
.quote-form .ttl{position:absolute;top:-30px;left:16px;color:#fff;font-weight:700;font-size:13px;text-transform:uppercase}
.field{height:30px;border:1px solid #ddd;margin-bottom:10px}
.field.tall{height:70px}
.quote-form .btn{width:100%;text-align:center}
.arrow{position:absolute;top:282px;width:36px;height:36px;border-radius:50%;background:rgba(0,0,0,.4);display:flex;align-items:center;justify-content:center}

/* welcome */
.welcome{padding:40px 0;height:340px}
.welcome .wrap{display:flex;gap:50px}
.welcome .txt{flex:1}
.welcome h2{color:var(--heading);font-size:30px;margin-bottom:14px}
.welcome p{margin-bottom:18px;font-size:12px}
.video{width:420px}
.video h2{color:var(--heading);font-size:30px;margin-bottom:14px}
.video .ph{height:200px;background:
  linear-gradient(180deg,#cfe6f3 0 45%,#b9cdb0 45% 60%,#8fa98a 60% 78%,#777 78%)}
.play{position:absolute;left:50%;top:50%;transform:translate(-50%,-50%);width:56px;height:40px;border-radius:9px;background:var(--red);display:flex;align-items:center;justify-content:center}

/* about */
.about{background:var(--light);height:460px;padding-top:50px}
.about-grid{display:flex;gap:40px}
.about-item{flex:1}
.about-item .ph{height:160px;margin-bottom:14px}
.about-item h4{color:var(--green);font-size:16px;margin-bottom:6px}
.about-item p{font-size:11px;margin-bottom:8px}

/* team */
.team{height:600px;padding-top:62px}
.team .intro{text-align:center;font-size:11px;width:900px;margin:-12px auto 30px}
.team-grid{display:flex;gap:16px}
.doc{flex:1}
.doc .ph{height:240px}
.doc .cap{background:var(--orange);color:#fff;text-align:center;padding:12px 0;height:68px}
.doc .cap h4{font-size:16px;line-height:1.3}
.doc .cap span{font-size:11px}
.plus{position:absolute;left:50%;top:50%;transform:translate(-50%,-50%)}

/* testimonials */
.happy{height:420px;padding-top:40px}
.testi-grid{display:flex;gap:60px}
.testi{flex:1;display:flex;gap:24px;align-items:center}
.testi .ph{width:150px;height:150px;border-radius:50%;flex:none}
.testi .q{color:var(--green);font-family:"Roboto Slab",Georgia,serif;font-size:34px;line-height:1;display:block;height:22px}
.testi p{font-size:11px;margin-bottom:10px}
.testi b{color:var(--orange);font-size:11px}
.dots{text-align:center;margin-top:22px}
.dots i{display:inline-block;width:9px;height:9px;border-radius:50%;background:#ccc;margin:0 3px}
.dots i.on{background:var(--orange)}

/* partners */
.partners{height:300px;padding-top:20px}
.partner-row{display:flex;justify-content:space-between;align-items:center}
.badge{width:250px;height:84px;border:1px solid #ddd;display:flex;align-items:center;justify-content:center;gap:14px}
.badge .mark{width:44px;height:44px;border-radius:50%}
.badge .bar{width:130px;height:30px;border-radius:4px}

/* contact */
.contact{height:280px;padding-top:30px}
.contact-grid{display:flex;gap:40px;border-top:1px solid #ddd;padding-top:30px}
.contact-brand{width:260px;text-align:center}
.contact-brand .brand{justify-content:center;margin-bottom:20px}
.contact-brand .brand-name{font-size:22px}
.office{flex:1;font-size:11px}
.office h4{color:var(--green);font-size:14px;margin-bottom:6px}

/* footer */
.footer{background:var(--footer);height:140px;color:#ccc}
.footer .wrap{display:flex;align-items:center;height:140px;gap:60px}
.footer .item{display:flex;align-items:center;gap:10px;font-size:18px}
.footer .social{margin-left:auto;display:flex;gap:8px}
.footer .social i{width:30px;height:30px;border-radius:50%;border:1px solid var(--orange)}
.copy{background:var(--orange);height:68px;color:#fff;font-size:11px}
.copy .wrap{display:flex;align-items:center;height:68px}
</style>
</head>
<body>

<header>
  <div class="wrap topbar">
    <div class="brand"><span class="brand-dot"></span><span class="brand-name">Kelvora Home Care</span></div>
    <div class="top-right">
      <div class="call"><small>CALL FOR A FREE EVALUATION TODAY</small><strong>555-010-4821</strong></div>
      <span class="btn">Login</span><span class="btn">Register</span>
    </div>
  </div>
  <nav class="nav"><div class="wrap"><ul><li>Home</li><li>About Us</li><li>Services</li><li>Our Network</li><li>Partner With Us</li><li>Contact Us</li></ul></div></nav>
</header>

<section class="hero" role="img" aria-label="Photo of a doctor caring for a young patient with her family">
  <span class="arrow" style="left:20px"><svg width="14" height="14" viewBox="0 0 14 14"><path d="M9 2L4 7l5 5" fill="none" stroke="#fff" stroke-width="2"/></svg></span>
  <span class="arrow" style="right:20px"><svg width="14" height="14" viewBox="0 0 14 14"><path d="M5 2l5 5-5 5" fill="none" stroke="#fff" stroke-width="2"/></svg></span>
  <div class="hero-circle">
    <h1>Kelvora Home Care</h1>
    <p>Trusted care at home for the families you left behind. We visit, check in and report back so you always know your loved ones are well looked after.</p>
    <span class="btn">Read More</span>
  </div>
  <form class="quote-form">
    <span class="ttl">Request More Information</span>
    <div class="field"></div><div class="field"></div><div class="field"></div><div class="field"></div><div class="field tall"></div>
    <span class="btn">Send</span>
  </form>
</section>

<section class="welcome">
  <div class="wrap">
    <div class="txt">
      <h2>Welcome to Kelvora Home Care</h2>
      <p>We help families living abroad look after parents and relatives in India. Our team arranges doctor visits, nursing, tests and daily support at home, and keeps you informed at every step. Each plan is shaped around the needs of your family and the advice of trusted local doctors. With a wide network of hospitals, clinics and care staff, help is never far away, day or night. You can follow every visit, report and bill from anywhere in the world, and speak to a care manager whenever you need.</p>
      <span class="btn">Learn More</span>
    </div>
    <div class="video">
      <h2>Watch a Video</h2>
      <div class="ph" role="img" aria-label="Video preview of a care team arriving at a family home">
        <span class="play"><svg width="18" height="20" viewBox="0 0 18 20"><path d="M2 1l15 9-15 9z" fill="#fff"/></svg></span>
      </div>
    </div>
  </div>
</section>

<section class="about">
  <div class="wrap">
    <h2 class="section-title">Get To Know More About Us</h2>
    <div class="about-grid">
      <div class="about-item"><div class="ph" style="background:radial-gradient(ellipse 90px 110px at 30% 55%,#fff,transparent 70%),radial-gradient(ellipse 120px 80px at 75% 40%,#7fa6c4,transparent 70%),linear-gradient(135deg,#cfdde6,#eef2f4)" role="img" aria-label="Doctor reviewing a patient file"></div><h4>What We Do</h4><p>We bring doctors, nurses and care staff to your family's door and keep you updated on their health.</p><span class="more">Read More</span></div>
      <div class="about-item"><div class="ph" style="background:radial-gradient(ellipse 130px 90px at 50% 50%,#b8c4cc,transparent 70%),linear-gradient(135deg,#4e5d69,#9aa8b2)" role="img" aria-label="Medical icons over a network background"></div><h4>Who We Are</h4><p>A team of care managers and clinicians who understand the worries of families living far from home.</p><span class="more">Read More</span></div>
      <div class="about-item"><div class="ph" style="background:radial-gradient(ellipse 90px 110px at 70% 55%,#f3e3d3,transparent 70%),radial-gradient(ellipse 100px 120px at 25% 50%,#6fa3c7,transparent 70%),linear-gradient(135deg,#9fc4d8,#e7eef2)" role="img" aria-label="Nurse smiling with an elderly patient"></div><h4>Why Do</h4><p>Because every parent deserves attentive care, and every child abroad deserves peace of mind.</p><span class="more">Read More</span></div>
    </div>
  </div>
</section>

<section class="team">
  <div class="wrap">
    <h2 class="section-title">Our Team</h2>
    <p class="intro">Our doctors bring years of practice across many fields of medicine. They work closely with our care managers to plan treatment, visit patients at home and guide families through every decision.</p>
    <div class="team-grid">
      <div class="doc"><div class="ph" style="background:radial-gradient(ellipse 70px 90px at 50% 42%,#c89b7a,transparent 72%),radial-gradient(ellipse 140px 80px at 50% 100%,#3c4a66,transparent 75%),linear-gradient(180deg,#d7b98a,#8a6e4e)" role="img" aria-label="Portrait of Dr. Arvin Mehra"></div><div class="cap"><h4>Dr. Arvin Mehra</h4><span>Radiation Oncology</span></div></div>
      <div class="doc"><div class="ph" style="background:linear-gradient(180deg,#6fb36f,#3d9a40)" role="img" aria-label="Placeholder portrait of Dr Tarun Bhalla"><svg class="plus" width="60" height="60" viewBox="0 0 60 60"><path d="M30 6v48M6 30h48" stroke="rgba(255,255,255,.8)" stroke-width="8"/></svg></div><div class="cap"><h4>Dr Tarun Bhalla</h4><span>Cardiology</span></div></div>
      <div class="doc"><div class="ph" style="background:radial-gradient(ellipse 70px 90px at 50% 40%,#a07a60,transparent 72%),radial-gradient(ellipse 140px 80px at 50% 100%,#2f3a52,transparent 75%),linear-gradient(180deg,#9ea8b6,#5a6475)" role="img" aria-label="Portrait of Dr. Naveen Kumar Oberoi"></div><div class="cap"><h4>Dr. Naveen Kumar Oberoi</h4><span>Neurosurgery</span></div></div>
      <div class="doc"><div class="ph" style="background:radial-gradient(ellipse 70px 50px at 50% 22%,#2f7fcf,transparent 72%),radial-gradient(ellipse 70px 80px at 50% 50%,#c99a78,transparent 72%),radial-gradient(ellipse 140px 80px at 50% 100%,#222,transparent 75%),linear-gradient(180deg,#cfd9e4,#7f8fa3)" role="img" aria-label="Portrait of Dr Jasdev Rana"></div><div class="cap"><h4>Dr Jasdev Rana</h4><span>Neurology</span></div></div>
    </div>
  </div>
</section>

<section class="happy">
  <div class="wrap">
    <h2 class="section-title">Happy Family</h2>
    <div class="testi-grid">
      <div class="testi"><div class="ph" style="background:radial-gradient(circle at 40% 45%,#e6cdb2,transparent 60%),linear-gradient(135deg,#d9c2a8,#8c7058)" role="img" aria-label="Photo of a smiling family member"></div><div><span class="q">“</span><p>Living overseas, I worried about my mother every day. The team visits her often, sends clear reports and calls me after each visit. It feels like family is there with her.</p><b>RAVI KAPOOR</b></div></div>
      <div class="testi"><div class="ph" style="background:radial-gradient(circle at 40% 45%,#e6cdb2,transparent 60%),linear-gradient(135deg,#d9c2a8,#8c7058)" role="img" aria-label="Photo of a smiling family member"></div><div><span class="q">“</span><p>When my father needed surgery, they arranged the hospital, the doctor and the nurse at home. Everything was handled with care and kindness from start to finish.</p><b>RAVI KAPOOR</b></div></div>
    </div>
    <div class="dots"><i class="on"></i><i></i><i></i></div>
  </div>
</section>

<section class="partners">
  <div class="wrap">
    <h2 class="section-title">Our Partner Hospitals</h2>
    <div class="partner-row">
      <div class="badge"><span class="mark" style="background:#3a8fd0"></span><span class="bar" style="background:#e8f0f7"></span></div>
      <div class="badge"><span class="mark" style="background:#1f4f8a"></span><span class="bar" style="background:#e3e9f2"></span></div>
      <div class="badge"><span class="mark" style="background:#d43a3a"></span><span class="bar" style="background:#f6e4e4"></span></div>
      <div class="badge"><span class="mark" style="background:#7a3fa0"></span><span class="bar" style="background:#eee6f3"></span></div>
    </div>
    <div class="dots"><i class="on"></i><i></i><i></i></div>
  </div>
</section>

<section class="contact">
  <div class="wrap">
    <h2 class="section-title">Kelvora Home Care Contact</h2>
    <div class="contact-grid">
      <div class="contact-brand"><div class="brand"><span class="brand-dot"></span><span class="brand-name">Kelvora Home Care</span></div><span class="btn">Get in Touch</span></div>
      <div class="office"><h4>Registered Office:</h4><p>Unit 12, Maple Court<br>Sector 4, Lakeview Road<br>Gurugram 122000<br>Haryana, India</p></div>
      <div class="office"><h4>Corporate Office:</h4><p>Plot 27, Green Avenue<br>Model Town Phase 2<br>Ludhiana 141000<br>Tel: 555-010-4821<br>Fax: 555-010-4822</p></div>
      <div class="office"><h4>Our US Office:</h4><p>418 Birchwood Lane<br>Suite 110<br>Fairview, CA 90000<br>United States</p></div>
    </div>
  </div>
</section>

<footer class="footer">
  <div class="wrap">
    <div class="item"><svg width="22" height="22" viewBox="0 0 24 24"><path d="M6.6 10.8a15 15 0 006.6 6.6l2.2-2.2a1 1 0 011-.25 11.4 11.4 0 003.6.57 1 1 0 011 1V20a1 1 0 01-1 1A17 17 0 013 4a1 1 0 011-1h3.5a1 1 0 011 1c0 1.25.2 2.45.57 3.57a1 1 0 01-.25 1z" fill="#ccc"/></svg>(01) 555-010-4821</div>
    <div class="item"><svg width="24" height="24" viewBox="0 0 24 24"><path d="M12 21s-8-5.3-8-11a4.5 4.5 0 018-2.8A4.5 4.5 0 0120 10c0 5.7-8 11-8 11z" fill="none" stroke="#ccc" stroke-width="2"/></svg></div>
    <div class="item"><svg width="24" height="18" viewBox="0 0 24 18"><rect x="1" y="1" width="22" height="16" fill="none" stroke="#ccc" stroke-width="2"/><path d="M1 1l11 9 11-9" fill="none" stroke="#ccc" stroke-width="2"/></svg>care@kelvorahomecare.com</div>
    <div class="social"><i></i><i></i><i></i><i></i><i></i><i></i><i></i><i></i></div>
  </div>
</footer>
<div class="copy"><div class="wrap">© Kelvora Home Care · 2024</div></div>

</body>
</html>
```